Manufacturers Catalog Cover Page

We are looking to have a cover to our catalog page designed. I currently have begun work for the remained of the catalog in InDesign and want the cover created in InDesign. I will provide photos.

Looking to beable to add the cover to our existing attached catalog.

Industry/Entity Type

Manufacturing

Requirements
Must have
• Colors match what we are currently using. The Dark grey and gold
Nice to have
• modern, clean

```html
<!DOCTYPE html>
<html lang="en">
<head>
<meta charset="utf-8">
<title>Catalog Spread – Gaskets, Trims &amp; Seals</title>
<link rel="stylesheet" href="https://fonts.googleapis.com/css2?family=Oswald:wght@500;600&family=Montserrat:wght@400;600&display=swap">
<style>
  :root {
    --backdrop: #8c8c8d;
    --charcoal: #3f3f41;
    --charcoal-deep: #333335;
    --charcoal-light: #4a4a4c;
    --gold: #c8b07a;
    --white: #ffffff;
    --muted: #d8d8d8;
  }
  * { margin: 0; padding: 0; box-sizing: border-box; }
  html, body { width: 908px; height: 1200px; overflow: hidden; background: var(--backdrop); }
  .canvas { position: relative; width: 908px; height: 1200px; }
  .spread {
    position: absolute; left: 0; top: 300px; width: 908px; height: 600px;
    display: flex; box-shadow: 0 10px 30px rgba(0,0,0,0.35);
  }
  .page-slot { position: relative; width: 454px; height: 600px; overflow: hidden; }
  .page {
    position: absolute; left: 0; top: 0; width: 908px; height: 1200px;
    transform: scale(0.5); transform-origin: 0 0;
    background: var(--charcoal); overflow: hidden; color: var(--white);
    font-family: "Oswald", "Arial Narrow", sans-serif;
  }
  .page-art { position: absolute; inset: 0; }

  /* Front cover */
  .cover-title { position: absolute; top: 58px; left: 0; right: 0; text-align: center; text-transform: uppercase; line-height: 1; }
  .cover-title__kicker { font-size: 30px; font-weight: 500; letter-spacing: 0.5px; }
  .cover-title__main { font-size: 56px; font-weight: 600; margin-top: 8px; letter-spacing: 0.5px; }
  .contact-block { position: absolute; right: 52px; top: 968px; text-align: right; font-weight: 500; text-transform: uppercase; }
  .contact-block__phone { font-size: 22px; line-height: 1.25; }
  .contact-block__web { font-size: 19px; margin-top: 44px; letter-spacing: 0.3px; }
  .brand { position: absolute; display: flex; align-items: center; }
  .brand--front { left: 52px; top: 1064px; gap: 20px; }
  .brand__circle { border-radius: 50%; border: 7px solid var(--gold); background: var(--charcoal-deep); }
  .brand--front .brand__circle { width: 84px; height: 84px; }
  .brand__name { font-weight: 500; line-height: 1.1; text-transform: uppercase; }
  .brand--front .brand__name { font-size: 28px; }

  /* Back cover */
  .brand--back { left: 150px; top: 180px; gap: 16px; }
  .brand--back .brand__circle { width: 66px; height: 66px; border-width: 6px; }
  .brand--back .brand__name { font-size: 24px; }
  .back-ring {
    position: absolute; left: 200px; top: 380px; width: 330px; height: 330px;
    border-radius: 50%; border: 16px solid rgba(200,176,122,0.28);
    background: rgba(255,255,255,0.04);
  }
  .contact-us { position: absolute; font-family: "Montserrat", sans-serif; width: 250px; }
  .contact-us--right { left: 560px; top: 700px; }
  .contact-us--left { left: 110px; top: 800px; }
  .contact-us__title { color: var(--gold); font-size: 24px; font-weight: 600; text-transform: uppercase; margin-bottom: 10px; }
  .contact-us__blurb { font-size: 13px; line-height: 1.35; color: var(--muted); margin-bottom: 12px; }
  .contact-us__line { display: flex; align-items: center; gap: 12px; font-size: 13px; color: var(--muted); margin-bottom: 7px; }
  .contact-us__line svg { flex: none; }
  .back-about { position: absolute; left: 110px; top: 1000px; width: 720px; font-family: "Montserrat", sans-serif; }
  .back-about__title { color: var(--gold); font-size: 22px; font-weight: 600; text-transform: uppercase; margin-bottom: 12px; }
  .back-about__text { font-size: 15px; line-height: 1.45; color: var(--muted); }
</style>
</head>
<body>
<main class="canvas">
  <div class="spread">

    <div class="page-slot">
      <section class="page page--back">
        <div class="brand brand--back">
          <span class="brand__circle"></span>
          <p class="brand__name">Meridian<br>Polymers</p>
        </div>
        <div class="back-ring"></div>

        <div class="contact-us contact-us--right">
          <h2 class="contact-us__title">Contact Us</h2>
          <p class="contact-us__blurb">Fast and quiet delivery for every seal, trim and gasket we make.</p>
          <p class="contact-us__line"><svg width="16" height="16" viewBox="0 0 16 16"><path d="M3 1h3l1 4-2 1a9 9 0 0 0 5 5l1-2 4 1v3a2 2 0 0 1-2 2A13 13 0 0 1 1 3a2 2 0 0 1 2-2z" fill="var(--gold)"/></svg>555-010-7788</p>
          <p class="contact-us__line"><svg width="16" height="16" viewBox="0 0 16 16"><rect x="1" y="3" width="14" height="10" rx="1" fill="none" stroke="var(--gold)" stroke-width="1.6"/><path d="M1 4l7 5 7-5" fill="none" stroke="var(--gold)" stroke-width="1.6"/></svg>info@meridianpolymers.com</p>
          <p class="contact-us__line"><svg width="16" height="16" viewBox="0 0 16 16"><circle cx="8" cy="8" r="6.5" fill="none" stroke="var(--gold)" stroke-width="1.6"/><path d="M1.5 8h13M8 1.5c-3 3.5-3 9.5 0 13M8 1.5c3 3.5 3 9.5 0 13" fill="none" stroke="var(--gold)" stroke-width="1.3"/></svg>www.meridianpolymers.com</p>
        </div>

        <div class="contact-us contact-us--left">
          <h2 class="contact-us__title">Contact Us</h2>
          <p class="contact-us__blurb">Fast and quiet delivery for every seal, trim and gasket we make.</p>
          <p class="contact-us__line"><svg width="16" height="16" viewBox="0 0 16 16"><path d="M3 1h3l1 4-2 1a9 9 0 0 0 5 5l1-2 4 1v3a2 2 0 0 1-2 2A13 13 0 0 1 1 3a2 2 0 0 1 2-2z" fill="var(--gold)"/></svg>555-010-7788</p>
          <p class="contact-us__line"><svg width="16" height="16" viewBox="0 0 16 16"><rect x="1" y="3" width="14" height="10" rx="1" fill="none" stroke="var(--gold)" stroke-width="1.6"/><path d="M1 4l7 5 7-5" fill="none" stroke="var(--gold)" stroke-width="1.6"/></svg>info@meridianpolymers.com</p>
          <p class="contact-us__line"><svg width="16" height="16" viewBox="0 0 16 16"><circle cx="8" cy="8" r="6.5" fill="none" stroke="var(--gold)" stroke-width="1.6"/><path d="M1.5 8h13M8 1.5c-3 3.5-3 9.5 0 13M8 1.5c3 3.5 3 9.5 0 13" fill="none" stroke="var(--gold)" stroke-width="1.3"/></svg>www.meridianpolymers.com</p>
        </div>

        <div class="back-about">
          <h2 class="back-about__title">Decum moltus ego vat, noca; hacerdit.</h2>
          <p class="back-about__text">Our extrusion lines shape rubber and plastic profiles for vehicles, boats, farm machines, buildings and plants. Every part is cut, checked and packed to your drawing, with short lead times and steady quality from the first sample to the last order.</p>
        </div>
      </section>
    </div>

    <div class="page-slot">
      <section class="page page--front">
        <svg class="page-art" width="908" height="1200" viewBox="0 0 908 1200" xmlns="http://www.w3.org/2000/svg">
          <defs>
            <polygon id="hex" points="-150,0 -75,-130 75,-130 150,0 75,130 -75,130"/>
            <linearGradient id="sky-rv" x1="0" y1="0" x2="0" y2="1"><stop offset="0" stop-color="#8fb6d6"/><stop offset="0.55" stop-color="#b98a6c"/><stop offset="1" stop-color="#6c5a4c"/></linearGradient>
            <linearGradient id="profiles" x1="0" y1="0" x2="1" y2="1"><stop offset="0" stop-color="#f2f2f2"/><stop offset="0.5" stop-color="#3a3a3c"/><stop offset="1" stop-color="#2b5f9a"/></linearGradient>
            <linearGradient id="car" x1="0" y1="0" x2="0" y2="1"><stop offset="0" stop-color="#a9cbe8"/><stop offset="0.6" stop-color="#c7cbcd"/><stop offset="1" stop-color="#6f7a5a"/></linearGradient>
            <linearGradient id="boat" x1="0" y1="0" x2="0" y2="1"><stop offset="0" stop-color="#9fc3e3"/><stop offset="0.45" stop-color="#e8eef2"/><stop offset="1" stop-color="#1f5e8f"/></linearGradient>
            <linearGradient id="robots" x1="0" y1="0" x2="1" y2="1"><stop offset="0" stop-color="#dfe7ee"/><stop offset="0.5" stop-color="#e2c23a"/><stop offset="1" stop-color="#7a8a99"/></linearGradient>
            <linearGradient id="harvester" x1="0" y1="0" x2="0" y2="1"><stop offset="0" stop-color="#7fb1dc"/><stop offset="0.5" stop-color="#e3c04a"/><stop offset="1" stop-color="#b79a62"/></linearGradient>
            <linearGradient id="building" x1="0" y1="0" x2="1" y2="1"><stop offset="0" stop-color="#e8eef4"/><stop offset="1" stop-color="#7f97ac"/></linearGradient>
            <linearGradient id="refinery" x1="0" y1="0" x2="0" y2="1"><stop offset="0" stop-color="#a8c4e0"/><stop offset="0.5" stop-color="#c7a384"/><stop offset="1" stop-color="#5f7f9f"/></linearGradient>
            <linearGradient id="strips" x1="0" y1="0" x2="1" y2="1"><stop offset="0" stop-color="#f4f4f4"/><stop offset="0.5" stop-color="#c9403a"/><stop offset="1" stop-color="#c7a27a"/></linearGradient>
            <linearGradient id="excavator" x1="0" y1="0" x2="0" y2="1"><stop offset="0" stop-color="#3d8fd6"/><stop offset="0.55" stop-color="#e0a23a"/><stop offset="1" stop-color="#a86f3e"/></linearGradient>
          </defs>
          <polygon fill="var(--gold)" points="0,250 908,150 908,250 0,350"/>
          <polygon fill="var(--gold)" points="0,890 908,800 908,900 0,1010"/>
          <g stroke="var(--charcoal)" stroke-width="12">
            <use href="#hex" x="95" y="420" fill="url(#sky-rv)" role="img" aria-label="Photo: motorhome on a desert road"/>
            <use href="#hex" x="95" y="692" fill="url(#building)" role="img" aria-label="Photo: modern office building"/>
            <use href="#hex" x="330" y="284" fill="url(#profiles)" role="img" aria-label="Photo: coiled rubber extrusion profiles"/>
            <use href="#hex" x="330" y="556" fill="url(#harvester)" role="img" aria-label="Photo: combine harvester in a field"/>
            <use href="#hex" x="330" y="828" fill="url(#refinery)" role="img" aria-label="Photo: industrial plant reflected in water"/>
            <use href="#hex" x="565" y="420" fill="url(#boat)" role="img" aria-label="Photo: speedboat on open water"/>
            <use href="#hex" x="565" y="692" fill="url(#strips)" role="img" aria-label="Photo: rolled sealing strips"/>
            <use href="#hex" x="800" y="284" fill="url(#car)" role="img" aria-label="Photo: silver car"/>
            <use href="#hex" x="800" y="556" fill="url(#excavator)" role="img" aria-label="Photo: backhoe excavator on a site"/>
            <use href="#hex" x="800" y="828" fill="url(#robots)" role="img" aria-label="Photo: robotic assembly line"/>
          </g>
        </svg>
        <header class="cover-title">
          <p class="cover-title__kicker">Rubber &amp; Plastic Extursion</p>
          <h1 class="cover-title__main">Gaskets, Trims &amp; Seals</h1>
        </header>
        <div class="contact-block">
          <p class="contact-block__phone">555-010-4821</p>
          <p class="contact-block__phone">555-010-2273</p>
          <p class="contact-block__web">www.meridianpolymers.com</p>
        </div>
        <div class="brand brand--front">
          <span class="brand__circle"></span>
          <p class="brand__name">Meridian<br>Polymers</p>
        </div>
      </section>
    </div>

  </div>
</main>
</body>
</html>
```